Velmarine - Mechanic/Collision Center Business Card

We're looking for a business card design for our mechanic/ collision repair shop.

Can be with colours or monochromatic.

See the attached files.

Many thanks

```html
<!DOCTYPE html>
<html lang="en">
<head>
<meta charset="utf-8">
<title>Velmarine – Business Card</title>
<link rel="stylesheet" href="https://fonts.googleapis.com/css2?family=Open+Sans:wght@400;600;700;800&display=swap">
<style>
  :root {
    --page-bg: #e9e9ec;
    --card-grey: #6e6e72;
    --grey-dark: #505054;
    --sky: #78b6e3;
    --sky-deep: #3a9ad9;
    --ink: #141414;
    --white: #ffffff;
  }
  * { margin: 0; padding: 0; box-sizing: border-box; }
  html, body { width: 1200px; height: 835px; overflow: hidden; }
  body {
    background: var(--page-bg);
    font-family: "Open Sans", Arial, sans-serif;
    display: flex;
    align-items: center;
    justify-content: center;
    gap: 40px;
  }
  .card {
    position: relative;
    width: 540px;
    height: 309px;
    border-radius: 18px;
    overflow: hidden;
    background: var(--card-grey);
    box-shadow: 0 6px 18px rgba(0,0,0,.18);
  }
  .card-shapes { position: absolute; inset: 0; }
  .front-info {
    position: absolute;
    left: 26px;
    top: 22px;
    color: var(--ink);
  }
  .brand-mark {
    display: flex;
    align-items: center;
    gap: 8px;
    font-weight: 800;
    font-size: 26px;
    letter-spacing: .5px;
    text-transform: uppercase;
    line-height: 1;
  }
  .brand-dot {
    width: 20px; height: 20px; border-radius: 50%;
    background: currentColor;
  }
  .company { font-size: 21px; font-weight: 600; margin-top: 12px; line-height: 1.1; }
  .role { font-size: 19px; font-weight: 600; line-height: 1.2; }
  .contacts { list-style: none; margin-top: 12px; }
  .contacts li {
    display: flex; align-items: center; gap: 8px;
    font-size: 14px; line-height: 21px; letter-spacing: .3px;
  }
  .contacts svg { width: 15px; height: 15px; flex: none; }
  .front-brand {
    position: absolute;
    right: 34px;
    top: 92px;
    color: var(--grey-dark);
  }
  .front-brand .brand-mark { font-size: 30px; }
  .back-badge {
    position: absolute;
    left: 50%; top: 50%;
    width: 180px; height: 180px;
    margin: -90px 0 0 -90px;
    border-radius: 50%;
    background: var(--white);
    border: 6px solid var(--sky-deep);
    box-shadow: 0 4px 14px rgba(0,0,0,.35);
    display: flex; align-items: center; justify-content: center;
    color: var(--ink);
  }
  .back-badge .brand-mark { font-size: 24px; gap: 6px; }
  .back-badge .brand-dot { width: 14px; height: 14px; background: var(--sky-deep); }
</style>
</head>
<body>

<section class="card card-front" aria-label="Front of business card">
  <svg class="card-shapes" viewBox="0 0 540 309" preserveAspectRatio="none" aria-hidden="true">
    <path d="M0 0 H262 Q330 235 540 296 V309 H0 Z" fill="var(--sky)"/>
    <path d="M0 0 H248 Q312 238 522 309 H0 Z" fill="var(--card-grey)"/>
    <path d="M0 0 H236 Q298 240 498 309 H0 Z" fill="var(--sky)"/>
  </svg>

  <div class="front-info">
    <div class="brand-mark"><span class="brand-dot"></span>Velmarine</div>
    <p class="company">Velmarine,LDA</p>
    <p class="role">founder &amp; CEO</p>
    <ul class="contacts">
      <li>
        <svg viewBox="0 0 16 16"><circle cx="8" cy="8" r="7" fill="none" stroke="currentColor" stroke-width="1.4"/><path d="M4.5 6.5h7v4h-7z" fill="currentColor"/></svg>
        +351210447382
      </li>
      <li>
        <svg viewBox="0 0 16 16"><rect x="4.5" y="1.5" width="7" height="13" rx="1.5" fill="none" stroke="currentColor" stroke-width="1.4"/><circle cx="8" cy="12" r=".9" fill="currentColor"/></svg>
        +351913582064
      </li>
      <li>
        <svg viewBox="0 0 16 16"><circle cx="8" cy="8" r="7" fill="none" stroke="currentColor" stroke-width="1.4"/><path d="M3 8h10M8 3v10" stroke="currentColor" stroke-width="1.2"/></svg>
        1170-318 Lisboa
      </li>
      <li>
        <svg viewBox="0 0 16 16"><circle cx="8" cy="8" r="7" fill="none" stroke="currentColor" stroke-width="1.4"/><path d="M8 12.5 5.3 8.2a3 3 0 1 1 5.4 0Z" fill="currentColor"/></svg>
        Rua Ferreira,42
      </li>
      <li>
        <svg viewBox="0 0 16 16"><circle cx="8" cy="8" r="7.5" fill="currentColor"/><path d="M4 5.5h8v5H4zM4 5.5l4 3 4-3" fill="none" stroke="var(--sky)" stroke-width="1.1"/></svg>
        velmarine.office@mailbox.pt
      </li>
      <li>
        <svg viewBox="0 0 16 16"><circle cx="8" cy="8" r="7" fill="none" stroke="currentColor" stroke-width="1.4"/></svg>
        www.velmarine-auto.pt/oficina
      </li>
    </ul>
  </div>

  <div class="front-brand">
    <div class="brand-mark"><span class="brand-dot"></span>Velmarine</div>
  </div>
</section>

<section class="card card-back" aria-label="Back of business card">
  <div class="back-badge">
    <div class="brand-mark"><span class="brand-dot"></span>Velmarine</div>
  </div>
</section>

</body>
</html>
```